I need a label created within the following dimensions below:

Label/Screen Printable Area:

Width 6.742”

Height 5.731”

The bottle dimensions are 7.175 (H) x 2.146 (D)

This is for 2 seperate labels.  One label for my hair Shampoo and another label for my hair Conditioner.

Requirements
Must have
• Front of Shampoo bottle:

Verdant Morning Roots logo

Product name (shampoo – Nourishing & Hydrating)

Bottle volume: 12 fl. Oz. (355ml)

Side of bottle:

"Verdant Strengthening with pure oil Essentials"

Back of bottle:

Verdant Morning Roots Shampoo is a blend of heavenly, ingredients from Mother Earth that nourish, protect and beautify your hair and extend the life of color. Our Products are Sulfate-Free, Paraben-Free, Contain No Artificial Colors and are Not Tested on Animals.

Distributed By and/or Get more information: (Distributed By: Morning Roots, Elmbrook, IL 60999/ Get more information and connect with Morning Roots at www.verdantmorningroots.com)

Ingredients: (I’ve included the ingredients listings below for quick copying to your art file)

DESCRIPTION: Morning Roots Shampoo

How to/ Directions for use: (Apply to wet hair. Massage into a rich lather. Rinse. Repeat if necessary.)

INGREDIENTS: Purified Water, Sodium Methyl 2-Sulfolaurate & Disodium 2-Sulfolaurate & Cocamidopropyl Betaine, Cetrimonium Chloride, Distearyl Phthalic Acid Amide, Simmondsia Chinensis (Organic Jojoba Seed) Oil, Butyrospermum Parkii (Organic Shea Butter) Fruit, Aloe Barbadensis Leaf Juice (Organic Aloe Vera Gel), Hydrolyzed Quinoa (Protein), Dimethicone, Fragrance (Apple, Pear, White Grape), Gluconolactone & Sodium Benzoate (Natural Preservative), Panthenol (Vitamin B-5), Citric Acid, Tocopherol (Vitamin E).

Front of conditioner bottle:

Product name: (Conditioner Shampoo - luxurious volume conditioner)

Side of bottle:

Back of bottle:

DESCRIPTION: Morning Roots Restructurant Conditioner

How to/ Directions for use: (Apply to wet hair. Massage into hair and sit for 5 minutes. For a deep conditoner treatment apply to hair and sit under the hair dryer for 20-30 minutes, Repeat if necessary; then rinse and style as usual).

INGREDIENTS: Purified Water, Behentrimonium Methosulfate (Modified Rapseed Oil), Cetearyl Alcohol, Cetyl Alcohol, Cetrimonium Chloride, Cyclopentasiloxane and Dimethicone, Caprylic/Capric Triglyceride, Extracts of Foeniculum Vulgare (Fennel Seed) and Helianthus Annuus (Sunflower Seed), Simmondsia Chinensis (Jojoba Seed) Oil, Olea Europaea (Olive Fruit) Oil, Fragrance, Mentha Piperita (Peppermint) Oil, Mentha (Menthol), Aloe Barbadensis Leaf Juice (Organic Aloe Vera Gel), Hydrolyzed Hair Keratin, Butyrospermum Parkii (Organic Shea Butter) Fruit, Sodium Benzoate (Natural Preservative) and Potassium Sorbate, Rosmarinus Officinalis (Rosemary) Oil, Lavandula Officinalis (Lavender) Oil, Panthenol (Vitamin B-5), Tocopherol (Vitamin E), Guar Hydroxypropyltrimonium Chloride, Citric Acid.

Width 6.742”

Height 5.731”

Should not have
• No other colors then what my logo colors currently are.

```html
<!DOCTYPE html>
<html lang="en">
<head>
<meta charset="utf-8">
<title>Verdant Morning Roots – Luxurious Volume Conditioner Label</title>
<link href="https://fonts.googleapis.com/css2?family=Open+Sans:ital,wght@0,400;0,600;0,700;1,400;1,600;1,700&display=swap" rel="stylesheet">
<style>
  :root {
    --gold: #a8812c;
    --green: #0f4d33;
    --paper: #ffffff;
  }
  html, body {
    margin: 0;
    padding: 0;
    width: 1200px;
    height: 1016px;
    overflow: hidden;
    background: var(--paper);
  }
  .label {
    position: relative;
    width: 1200px;
    height: 1016px;
    overflow: hidden;
    background: var(--paper);
    font-family: "Open Sans", sans-serif;
    color: var(--green);
  }

  /* Side spines */
  .spine {
    position: absolute;
    top: 508px;
    width: 700px;
    margin-left: -350px;
    text-align: center;
    transform: translateY(-50%) rotate(-90deg);
    font-style: italic;
    font-size: 33px;
    letter-spacing: 1.5px;
    color: var(--gold);
    white-space: nowrap;
  }
  .spine strong { font-weight: 700; }
  .spine--left { left: 77px; }
  .spine--right { left: 707px; }

  /* Brand name blocks */
  .brand {
    position: absolute;
    text-align: center;
    color: var(--green);
    font-weight: 600;
  }
  .brand__dot {
    display: block;
    margin: 0 auto 10px;
    border-radius: 50%;
    background: var(--gold);
  }
  .brand--back { left: 234px; width: 300px; top: 48px; font-size: 25px; line-height: 1.15; }
  .brand--back .brand__dot { width: 22px; height: 22px; }
  .brand--front { left: 792px; width: 380px; top: 90px; font-size: 36px; line-height: 1.15; }
  .brand--front .brand__dot { width: 32px; height: 32px; margin-bottom: 18px; }

  /* Product title */
  .product-title {
    position: absolute;
    display: flex;
    align-items: center;
  }
  .product-title__kicker {
    color: var(--gold);
    font-style: italic;
    text-transform: uppercase;
    text-align: right;
    line-height: 1;
  }
  .pill {
    display: inline-block;
    background: var(--gold);
    color: var(--paper);
    font-style: italic;
    font-weight: 700;
    border-radius: 0 12px 0 12px;
  }
  .product-title--back { left: 212px; top: 191px; }
  .product-title--back .product-title__kicker { font-size: 20px; margin-right: 6px; }
  .product-title--back .pill { font-size: 29px; padding: 1px 12px 2px; }

  /* Back copy */
  .back-copy {
    position: absolute;
    left: 160px;
    width: 448px;
    text-align: center;
    font-style: italic;
  }
  .intro {
    top: 244px;
    color: var(--gold);
    font-weight: 600;
    font-size: 15px;
    line-height: 22.3px;
    margin: 0;
  }
  .section-head {
    position: absolute;
    left: 0;
    right: 0;
    text-align: center;
  }
  .section-head .pill {
    font-weight: 600;
    font-size: 19px;
    padding: 0 11px 1px;
    border-radius: 0 10px 0 10px;
  }
  .directions-head { top: 392px; left: 160px; width: 448px; }
  .directions {
    top: 425px;
    font-size: 14.4px;
    line-height: 19.2px;
    margin: 0;
  }
  .ingredients-head { top: 527px; left: 160px; width: 448px; }
  .ingredients {
    top: 563px;
    font-size: 14.4px;
    line-height: 22.2px;
    margin: 0;
  }
  .distributor {
    top: 888px;
    font-size: 14.4px;
    line-height: 19px;
    margin: 0;
  }
  .distributor__title {
    display: block;
    color: var(--gold);
    font-weight: 700;
    font-size: 19.5px;
    line-height: 24px;
  }
  .distributor__web {
    display: block;
    color: var(--gold);
    font-weight: 700;
    font-size: 16.5px;
    line-height: 24px;
    letter-spacing: 0.3px;
  }

  /* Front panel */
  .aloe-art {
    position: absolute;
    left: 812px;
    top: 368px;
    width: 308px;
    height: 272px;
  }
  .front-name {
    position: absolute;
    left: 802px;
    width: 360px;
    top: 668px;
    text-align: center;
    color: var(--gold);
    font-size: 30px;
    line-height: 31px;
    text-transform: uppercase;
  }
  .front-pill {
    position: absolute;
    left: 864px;
    top: 742px;
    width: 242px;
    height: 51px;
    line-height: 51px;
    text-align: center;
    font-size: 31px;
    padding: 0;
    border-radius: 0 14px 0 14px;
  }
  .front-tagline {
    position: absolute;
    left: 832px;
    width: 300px;
    top: 804px;
    text-align: center;
    font-style: italic;
    font-size: 16px;
    line-height: 20px;
    margin: 0;
  }
  .front-tagline strong { font-weight: 700; }
  .volume {
    position: absolute;
    left: 832px;
    width: 300px;
    top: 958px;
    text-align: center;
    font-weight: 600;
    font-size: 15px;
    color: #1a1a1a;
    margin: 0;
  }
</style>
</head>
<body>
<main class="label">

  <!-- Back panel -->
  <div class="spine spine--left">Verdant Strengthening with <strong>Pure Oil</strong> Essentials</div>

  <div class="brand brand--back">
    <span class="brand__dot"></span>
    Verdant Morning Roots
  </div>

  <div class="product-title product-title--back">
    <span class="product-title__kicker">Luxurious<br>Volume</span>
    <span class="pill">CONDITIONER</span>
  </div>

  <p class="back-copy intro">Verdant Morning Roots Conditioner is a blend of heavenly, ingredients from Mother Earth that nourish, protect and beautify your hair and extend the life of color. Our Products are Sulfate-Free, Paraben-Free, Contain No Artificial Colors and are Not Tested on Animals.</p>

  <div class="section-head directions-head"><span class="pill">Directions for use</span></div>
  <p class="back-copy directions">Apply to wet hair. Massage into hair and sit for 5 minutes. For a deep conditoner treatment apply to hair and sit under the hair dryer for 20-30 minutes, Repeat if necessary; then rinse and style as usual</p>

  <div class="section-head ingredients-head"><span class="pill">Ingredients</span></div>
  <p class="back-copy ingredients">Purified Water, Behentrimonium Methosulfate (Modified Rapseed Oil), Cetearyl Alcohol, Cetyl Alcohol, Cetrimonium Chloride, Cyclopentasiloxane and Dimethicone, Caprylic/Capric Triglyceride, Extracts of Foeniculum Vulgare (Fennel Seed) and Helianthus Annuus (Sunflower Seed), Simmondsia Chinensis (Jojoba Seed) Oil, Olea Europaea (Olive Fruit) Oil, Fragrance, Mentha Piperita (Peppermint) Oil, Mentha (Menthol), Aloe Barbadensis Leaf Juice (Organic Aloe Vera Gel), Hydrolyzed Hair Keratin, Butyrospermum Parkii (Organic Shea Butter) Fruit, Sodium Benzoate (Natural Preservative) and Potassium Sorbate, Rosmarinus Officinalis (Rosemary) Oil, Lavandula Officinalis (Lavender) Oil, Panthenol (Vitamin B-5), Tocopherol (Vitamin E), Guar Hydroxypropyltrimonium Chloride, Citric Acid.</p>

  <p class="back-copy distributor">
    <span class="distributor__title">Distributed By</span>
    Morning Roots, Elmbrook, IL 60999<br>
    Get more information and connect<br>
    with Morning Roots at
    <span class="distributor__web">www.verdantmorningroots.com</span>
  </p>

  <!-- Front panel -->
  <div class="spine spine--right">Verdant Strengthening with <strong>Pure Oil</strong> Essentials</div>

  <div class="brand brand--front">
    <span class="brand__dot"></span>
    Verdant Morning Roots
  </div>

  <svg class="aloe-art" viewBox="0 0 308 272" role="img" aria-label="Illustration of an aloe vera plant with two hanging seed pods">
    <defs>
      <radialGradient id="aloeTone" cx="50%" cy="70%" r="60%">
        <stop offset="0%" stop-color="#0f4d33"/>
        <stop offset="75%" stop-color="#3f6b3a"/>
        <stop offset="100%" stop-color="#a8812c" stop-opacity="0.55"/>
      </radialGradient>
    </defs>
    <rect width="308" height="272" rx="18" fill="url(#aloeTone)"/>
  </svg>

  <div class="front-name">Luxurious<br>Volume</div>
  <div class="pill front-pill">CONDITIONER</div>
  <p class="front-tagline">Verdant Strengthening<br>with <strong>Pure Oil</strong> Essentials</p>

  <p class="volume">12 fl. Oz. (355ml)</p>

</main>
</body>
</html>
```